Business Card Design Project (Beer industry)

I am seeking a redesign of my business card. I am looking for something that will really stand out in both texture and feel. Something more on the modern side then traditional. Nothing die cut shaped like a beer mug please.

The card is used mostly for other industry professionals, as well as bar and restaurant owners. My title is Strategy & Acquisitions. If you would like to somehow incorporate that theme, that may work.

My business is craft and imported beer. Nothing fizzy and yellow, so my products are more on the upscale side.
Updates

I was able to update my logo in .ai and .tif format. I hope that helps. 

Thank you all for your creative ideas. I have uploaded my current business card in pdf format, as well as our logo in .eps file format. We are excited about the submissions so far and want to thank you all again.

PS Please do not include fax number in future submissions, as we are looking for something more creative and a fax says 1999 and not 2015, which is the message we are going for, without being futuristic. 

Thank you all once again for all of your submissions. If we would consider a two sided card, we would like the opposite side not to be the same as the front. The styles we have seen so far, it appears the front and back are too similar. Again, a two sided card is not required. Thank you and we look forward to pushing the boundaries of your creativity. Cheers

Target Market(s)

My card would mostly go to bar and restaurant operators as well as other beer industry professionals

Industry/Entity Type

Restaurant

Requirements
Nice to have
• Two sided would be considered, although not required
Should not have
• Anything die cut shaped like a beer mug.

```html
<!DOCTYPE html>
<html lang="en">
<head>
<meta charset="utf-8">
<title>Harbor Tap – Business Card</title>
<link href="https://fonts.googleapis.com/css2?family=Arvo:ital,wght@0,400;0,700;1,400&family=Arimo:wght@400;700&display=swap" rel="stylesheet">
<style>
  :root {
    --page-bg: #e9e6e1;
    --card-white: #ffffff;
    --band-blue: #3a7fc0;
    --ink: #1d1d1d;
    --ink-soft: #444444;
    --orange-light: #f3a526;
    --orange-deep: #de7417;
    --brand-red: #a3222b;
    --brand-navy: #2b4b86;
    --tagline-brown: #5b3a1c;
  }
  * { box-sizing: border-box; margin: 0; padding: 0; }
  html, body { width: 1200px; height: 900px; overflow: hidden; }
  body {
    background: var(--page-bg);
    display: flex;
    align-items: center;
    justify-content: center;
    gap: 40px;
    font-family: "Arimo", Arial, sans-serif;
  }
  .card {
    position: relative;
    width: 540px;
    height: 309px;
    border-radius: 3px;
    overflow: hidden;
    box-shadow: 0 6px 18px rgba(0,0,0,0.18);
  }

  /* Front */
  .card-front { background: var(--card-white); }
  .holder { position: absolute; right: 38px; top: 34px; text-align: right; }
  .holder-name {
    font-family: "Arvo", Georgia, serif;
    font-weight: 700;
    font-size: 27px;
    letter-spacing: 2px;
    color: var(--ink);
  }
  .holder-title { font-size: 10px; color: var(--ink-soft); margin-top: 2px; }
  .contacts { position: absolute; left: 282px; top: 118px; list-style: none; }
  .contact { display: flex; align-items: center; height: 30px; font-size: 13px; color: var(--ink); }
  .contact-label {
    width: 50px;
    font-family: "Arvo", Georgia, serif;
    font-weight: 700;
    font-size: 9px;
    letter-spacing: 1px;
    color: var(--ink-soft);
    border-top: 1px solid var(--ink-soft);
    border-bottom: 1px solid var(--ink-soft);
    text-align: center;
    margin-right: 14px;
    line-height: 12px;
  }
  .brand-front {
    position: absolute; left: 40px; top: 150px;
    display: flex; align-items: center; gap: 8px;
  }
  .brand-dot { width: 14px; height: 14px; border-radius: 50%; background: var(--brand-red); }
  .brand-name {
    font-family: "Arvo", Georgia, serif;
    font-weight: 700;
    font-size: 24px;
    color: var(--brand-red);
  }
  .info-band {
    position: absolute; left: 0; right: 0; bottom: 0;
    height: 66px;
    background: var(--band-blue);
    display: flex; align-items: center; justify-content: space-between;
    padding: 0 30px;
    color: #fff;
    font-size: 13px;
  }

  /* Back */
  .card-back {
    background: radial-gradient(ellipse at 55% 40%, var(--orange-light) 0%, var(--orange-deep) 75%);
    display: flex; flex-direction: column; align-items: center; justify-content: center;
  }
  .brand-back { display: flex; align-items: center; gap: 10px; }
  .brand-back .brand-name { font-size: 38px; }
  .brand-back .brand-dot { width: 20px; height: 20px; }
  .brand-city {
    font-family: "Arvo", Georgia, serif;
    font-size: 20px;
    color: var(--brand-navy);
    margin-top: 6px;
  }
  .brand-tagline {
    font-family: "Arvo", Georgia, serif;
    font-size: 11px;
    color: var(--tagline-brown);
    margin-top: 4px;
  }
</style>
</head>
<body>
  <section class="card card-front">
    <div class="holder">
      <h1 class="holder-name">DAN KORVEL</h1>
      <p class="holder-title">Strategy &amp; Acquisitions</p>
    </div>
    <ul class="contacts">
      <li class="contact"><span class="contact-label">CELL</span>(917) 555-0142</li>
      <li class="contact"><span class="contact-label">EMAIL</span>dkorvel@mailbox.com</li>
    </ul>
    <div class="brand-front">
      <span class="brand-dot"></span>
      <span class="brand-name">Harbor Tap</span>
    </div>
    <footer class="info-band">
      <span class="address">42 Foundry Street Brooklyn, NY 11200</span>
      <span class="website">www.harbortapbeer.com</span>
    </footer>
  </section>

  <section class="card card-back">
    <div class="brand-back">
      <span class="brand-dot"></span>
      <span class="brand-name">Harbor Tap</span>
    </div>
    <p class="brand-city">New York</p>
    <p class="brand-tagline">Premier Craft &amp; Import Beer Distributor</p>
  </section>
</body>
</html>
```